Business card design

We need a business card designed completed for a new company. We are a company that works with associations, schools to convert their older text/DVDs into dynamic online and mobile programs. Our initial platform is designed for the legal associations and will enable their lawyers to access their content such as forms, videos, case law and support materials anywhere, anytime. We are also focused on Project Management Associations, Financial Management Associations and IT Associations.

I would like for the business card to have the following information:

Logo

Carl vantreese

President and CEO

cvantreese@plumquarry.com

Mobile: 613-547-3918

www.plumquarry.com

Tag line: Transforming content into a mobile platform    

I would like it to be double sided, use the colours of the logo, tie into the mobile world

 

Industry/Entity Type

Legal

Logo Text

Plumquarry

```html
<!DOCTYPE html>
<html lang="en">
<head>
<meta charset="utf-8">
<title>Plumquarry business card</title>
<link rel="stylesheet" href="https://fonts.googleapis.com/css2?family=PT+Sans:wght@400;700&display=swap">
<style>
  :root {
    --backdrop: #e4e1dc;
    --label: #2a2a2a;
    --card-grey: #999999;
    --card-white: #ffffff;
    --band-dark: #666666;
    --band-mid: #8c8c8c;
    --band-light: #ffffff;
    --ink-dark: #333333;
    --ink-light: #ffffff;
    --logo-on-white: #777777;
  }
  * { margin: 0; padding: 0; box-sizing: border-box; }
  html, body { width: 1200px; height: 800px; overflow: hidden; }
  body {
    position: relative;
    background: var(--backdrop);
    font-family: "PT Sans", "Myriad Pro", Arial, sans-serif;
  }
  .side-label {
    position: absolute;
    width: 510px;
    text-align: center;
    font-size: 21px;
    color: var(--label);
  }
  .card {
    position: absolute;
    width: 510px;
    height: 291px;
    border-radius: 20px;
    overflow: hidden;
    box-shadow: 0 6px 14px rgba(0,0,0,0.28);
  }
  .card--grey { background: var(--card-grey); color: var(--ink-light); }
  .card--white { background: var(--card-white); color: var(--ink-dark); }
  .brand-name {
    position: absolute;
    left: 0; right: 0;
    text-align: center;
    font-weight: 700;
    line-height: 1;
  }
  .card--grey .brand-name { color: var(--ink-light); }
  .card--white .brand-name { color: var(--logo-on-white); }
  .detail .brand-name { top: 44px; font-size: 52px; }
  .cover .brand-name { top: 104px; font-size: 76px; }
  .person {
    position: absolute; top: 117px; left: 0; right: 0;
    text-align: center; font-size: 18px;
  }
  .person .role { font-size: 14px; }
  .mobile {
    position: absolute; top: 152px; left: 0; right: 0;
    text-align: center; font-size: 13px;
  }
  .mobile b { font-style: italic; }
  .bands { position: absolute; left: 0; top: 195px; }
  .email, .web {
    position: absolute; font-size: 14px;
  }
  .email { left: 51px; top: 203px; }
  .web { right: 50px; top: 221px; color: var(--ink-light); }
  .card--grey .email { color: var(--ink-dark); }
  .card--white .email { color: var(--ink-dark); }
  .tagline {
    position: absolute; top: 259px; left: 0; right: 0;
    text-align: center; font-size: 16px;
  }
  .cover .site {
    position: absolute; top: 253px; left: 0; right: 0;
    text-align: center; font-size: 17px; letter-spacing: 4px;
  }
  .card--grey.cover .site { color: var(--ink-dark); }
</style>
</head>
<body>
  <div class="side-label" style="left:74px; top:50px;">Front</div>
  <div class="side-label" style="left:632px; top:50px;">Back - 1</div>
  <div class="side-label" style="left:74px; top:409px;">Back - 2</div>
  <div class="side-label" style="left:632px; top:409px;">Back - 3</div>

  <section class="card card--grey detail" style="left:80px; top:97px;">
    <div class="brand-name">Plumquarry</div>
    <p class="person">Carl vantreese, <span class="role">President and CEO</span></p>
    <p class="mobile"><b>c</b> : 613-547-3918</p>
    <svg class="bands" width="510" height="55" viewBox="0 0 510 55">
      <polygon points="265,17 510,17 510,53 240,53" fill="var(--band-dark)"/>
      <polygon points="0,0 298,0 268,34 0,34" fill="var(--band-light)"/>
    </svg>
    <p class="email">cvantreese@plumquarry.com</p>
    <p class="web">www.plumquarry.com</p>
    <p class="tagline">Transforming content into a mobile platform</p>
  </section>

  <section class="card card--white detail" style="left:639px; top:97px;">
    <div class="brand-name">Plumquarry</div>
    <p class="person">Carl vantreese, <span class="role">President and CEO</span></p>
    <p class="mobile"><b>c</b> : 613-547-3918</p>
    <svg class="bands" width="510" height="55" viewBox="0 0 510 55">
      <polygon points="265,17 510,17 510,53 240,53" fill="var(--band-dark)"/>
      <polygon points="0,0 298,0 268,34 0,34" fill="var(--band-mid)"/>
    </svg>
    <p class="email">cvantreese@plumquarry.com</p>
    <p class="web">www.plumquarry.com</p>
    <p class="tagline">Transforming content into a mobile platform</p>
  </section>

  <section class="card card--grey cover" style="left:73px; top:452px;">
    <div class="brand-name">Plumquarry</div>
    <p class="site">www.plumquarry.com</p>
  </section>

  <section class="card card--white cover" style="left:634px; top:450px;">
    <div class="brand-name">Plumquarry</div>
    <p class="site">www.plumquarry.com</p>
  </section>
</body>
</html>
```